FACE HARBOR

Labels for Men's Skin Care. Organic, target 25-35 The label will be 2x3.5 on a 4oz amber bottle. 3 labels with the information shown on the uploaded sample.
Our product is a e-commerce built to help my 24 year old twin sons have a business of their own. Although it will be sold online they will also do foot work and sell to barbers at barber shops using as a mist on customers after shaving. So we want something that will attract male customers and will look good in a modern Barbershop. This is there shot and packaging is very very important. So if you could help us out with a great label we would be working with you in the future for package design. Our line will have several mens Organic natural skin care cleanser, mask toners and moisturizers..Thank you for your help. We also hope to put our products in beauty supply shops. So it needs to stand out as a mans product but still be traditional male product. Oh be creative mind that you are and remember we are trying to build a brand that attracts 25-35 male. Thank you

Hello, I just wanted to let you know that I am up working very late.

for anyone on the other side of the world up and working. I sleep about
3 hours.. So I'll be up for a few more hours and then up again around 5am my time

Good morning... I just wanted to say I will need three labels.. The words on all three are not that different and will fit pretty much the same on all three. So if you could work with one showing how the colors might be a little different on the other two you can do that with just the one label Just to make it easier on you if you like.. we can fix the other two once I find the right label,  Thank you it is 3am here.. still working.. I love it.

Target Market(s)

MALE 25-35

Industry/Entity Type

E-Commerce

Requirements
Must have
• final design must be fitted to the dieline uploaded.

```html
<!DOCTYPE html>
<html lang="en">
<head>
<meta charset="utf-8">
<title>Face Harbor – Men's Daily Edge Calm Label</title>
<link rel="stylesheet" href="https://fonts.googleapis.com/css2?family=Michroma&family=Tinos:wght@400;700&display=swap">
<style>
  :root {
    --page-bg: #f4f4f4;
    --page-bg-edge: #e6e6e6;
    --espresso: #2a1417;
    --brown: #3c1a11;
    --brown-warm: #42200f;
    --sage: #dfe8bf;
    --leaf: #d5e3a0;
    --olive: #7f9a3c;
    --royal: #0c3ea6;
    --royal-light: #3f78e6;
    --stripe-dark: #2d2038;
    --stripe-light: #9a8fa8;
    --white: #ffffff;
    --ink: #2a1a12;
  }
  html, body {
    margin: 0;
    padding: 0;
    width: 1200px;
    height: 922px;
    overflow: hidden;
  }
  body {
    background: radial-gradient(ellipse at 60% 40%, var(--page-bg) 0%, var(--page-bg-edge) 100%);
    position: relative;
    font-family: "Tinos", "Times New Roman", serif;
  }
  .label {
    position: absolute;
    left: 380px;
    top: 78px;
    width: 440px;
    height: 765px;
    overflow: hidden;
    box-shadow: 4px 6px 10px rgba(0,0,0,0.35);
  }
  .label__header {
    position: absolute;
    left: 0; top: 0;
    width: 440px; height: 234px;
    background: linear-gradient(to right, var(--espresso) 0 176px, var(--sage) 176px 100%);
  }
  .label__tree {
    position: absolute;
    left: 58px; top: 10px;
    width: 304px; height: 168px;
    border-radius: 50% 50% 40% 40%;
    background: radial-gradient(ellipse at 50% 40%, #a9c46a 0%, #6f8f34 55%, rgba(80,110,40,0.0) 80%);
  }
  .label__brand {
    position: absolute;
    left: 0; top: 180px;
    width: 440px;
    text-align: center;
    font-size: 38px;
    letter-spacing: 1px;
    color: var(--olive);
    line-height: 1;
  }
  .band {
    position: absolute;
    left: 0; width: 440px;
    background: linear-gradient(to bottom, var(--royal-light), var(--royal) 60%, #0a2f80);
  }
  .band--upper { top: 234px; height: 18px; }
  .band--lower { top: 383px; height: 13px; }
  .label__title {
    position: absolute;
    left: 0; top: 252px;
    width: 440px; height: 131px;
    background: var(--brown);
  }
  .stripes {
    position: absolute;
    background: linear-gradient(to right, var(--stripe-dark), var(--stripe-light) 50%, var(--stripe-dark));
  }
  .stripes--title { left: 0; top: 0; width: 40px; height: 131px; }
  .stripes--panel { left: 0; top: 396px; width: 176px; height: 369px; }
  .title__mens {
    position: absolute;
    left: 0; top: 14px;
    width: 440px;
    text-align: center;
    font-family: "Michroma", "Arial Black", sans-serif;
    font-size: 70px;
    line-height: 1;
    color: var(--leaf);
    letter-spacing: 2px;
  }
  .title__product {
    position: absolute;
    left: 0; top: 92px;
    width: 440px;
    text-align: center;
    font-size: 27px;
    line-height: 1;
    color: var(--leaf);
    letter-spacing: 2px;
  }
  .label__panel {
    position: absolute;
    left: 176px; top: 396px;
    width: 264px; height: 369px;
    background: var(--brown-warm);
    text-align: center;
  }
  .claim {
    margin: 0;
    color: var(--white);
    font-size: 21px;
    line-height: 23px;
    font-weight: 700;
    text-transform: uppercase;
    letter-spacing: 0.3px;
  }
  .claim--first { margin-top: 12px; }
  .claim__plus {
    margin: 0;
    color: var(--white);
    font-size: 40px;
    line-height: 32px;
  }
  .benefit {
    margin: 26px 12px 0;
    padding: 6px 0;
    background: var(--leaf);
    color: var(--ink);
    font-size: 21px;
    line-height: 22px;
  }
  .ingredients {
    margin: 24px 0 0;
    color: var(--leaf);
    font-size: 19px;
    line-height: 25px;
    font-variant: small-caps;
  }
  .volume {
    margin: 22px 0 0;
    color: var(--white);
    font-size: 18px;
  }
</style>
</head>
<body>
  <section class="label" aria-label="Face Harbor Men's Daily Edge Calm label">
    <div class="label__header">
      <div class="label__tree" role="img" aria-label="Illustration of a leafy green tree"></div>
      <div class="label__brand">FACE HARBOR</div>
    </div>
    <div class="band band--upper"></div>
    <div class="label__title">
      <div class="stripes stripes--title" role="img" aria-label="Vertical pinstripe pattern"></div>
      <div class="title__mens">MEN'S</div>
      <div class="title__product">DAILY EDGE CALM</div>
    </div>
    <div class="band band--lower"></div>
    <div class="stripes stripes--panel" role="img" aria-label="Vertical pinstripe pattern"></div>
    <div class="label__panel">
      <p class="claim claim--first">Treat and prevent<br>ingrown hair</p>
      <p class="claim__plus">+</p>
      <p class="claim">Calms razor burn<br>after shaving</p>
      <p class="benefit">Refresh + Moisturize</p>
      <p class="ingredients">Botanical Healing Mist<br>Acai Berry + Goats Milk</p>
      <p class="volume">3.5fl oz 103ml</p>
    </div>
  </section>
</body>
</html>
```